Content Website for Cycling products

Dear Participant,

I'm looking for a design for a workpress content website where innovative products will be featured (no sales, no e-commerce, no Google Ads), only own content.

The website will be called spokewise.com.

The idea of the site should be like the site of Brightforge Digest: https://brightforgedigest.com/
and Nimble Trove https://thenimbletrove.com/
Vanto Wares: http://www.vantowares.com/

Althogh I like the idea of these mentioned websites, I don't like there design and the way the content and products are presented. Especially the homepage and the above the fold content.

The design of spokewise.com should be more readable, more snackable, more enjoyable and less cluttered.

The product pages should feature a video of the product as well.

Here are some examples of the products that will be featured:
https://www.facebook.com/SpokeWise
https://www.linkedin.com/company/spokewise/videos/?viewAsMember=true

Looking forward to seeing some interesting designs and ideas!

PS: Deliverable should be clickable figma design.
PSS: Higher priority if you deliver a ready to use wordpress site.

```html
<!DOCTYPE html>
<html lang="en">
<head>
<meta charset="utf-8">
<title>SpokeWise – Innovative Cycling Products</title>
<link rel="stylesheet" href="https://fonts.googleapis.com/css2?family=Montserrat:ital,wght@0,300;0,400;0,500;0,700;1,700;1,800&display=swap">
<style>
  :root {
    --teal: #14c09c;
    --teal-dark: #10a988;
    --stage: #19bf98;
    --white: #ffffff;
    --ink: #111111;
    --muted: #3a3a3a;
    --photo-dark: #2c2d2f;
    --photo-night: #1b1b1d;
  }
  * { box-sizing: border-box; margin: 0; padding: 0; }
  html, body { width: 1200px; height: 824px; overflow: hidden; }
  body {
    background: var(--stage);
    font-family: "Montserrat", sans-serif;
    color: var(--ink);
    position: relative;
  }
  .page {
    position: absolute; left: 253px; top: 73px;
    width: 694px; height: 751px;
    background: linear-gradient(160deg, #eef8f8 0%, var(--white) 30%);
    border-radius: 13px 13px 0 0;
    overflow: hidden;
  }
  .abs { position: absolute; }

  /* header */
  .brand {
    left: 48px; top: 14px; width: 51px; height: 51px;
    border: 1.5px solid var(--ink); border-radius: 50%;
    display: flex; align-items: center; justify-content: center;
    font-size: 7px; font-weight: 700; letter-spacing: .5px; color: var(--ink);
  }
  .nav { top: 33px; display: flex; gap: 0; }
  .nav a { position: absolute; font-size: 9px; color: var(--teal); text-decoration: none; white-space: nowrap; }
  .subscribe {
    left: 568px; top: 24px; width: 77px; height: 29px;
    background: var(--teal); color: var(--white); border-radius: 15px;
    font-size: 8.5px; display: flex; align-items: center; justify-content: center;
  }

  /* hero */
  .hero-title { left: 48px; top: 84px; font-size: 26.5px; font-weight: 400; color: var(--teal); white-space: nowrap; }
  .hero-text { left: 48px; top: 122px; width: 330px; font-size: 8.6px; line-height: 11px; color: var(--ink); }
  .photo { border-radius: 10px; }
  .photo-handlebar { left: 48px; top: 201px; width: 327px; height: 217px;
    background: radial-gradient(ellipse at 50% 60%, #4a4c50 0%, var(--photo-dark) 70%); }
  .trending-card { left: 416px; top: 77px; width: 229px; height: 341px; overflow: hidden;
    background: linear-gradient(180deg, #b9c4cc 0%, #cfd6da 18%, #6f8a5a 30%, #7e8a90 45%, #5d6a72 70%, #3f4a52 100%); }
  .trending-title { left: 0; width: 229px; top: 345px; text-align: center; font-size: 25px; font-weight: 700; color: var(--white); left: 416px; }
  .trending-link { left: 416px; width: 229px; top: 396px; text-align: center; font-size: 8.5px; color: #e6e6e6; }

  /* posts */
  .section-title { left: 0; width: 694px; top: 464px; text-align: center; font-size: 25px; font-weight: 800; font-style: italic; color: var(--teal); }
  .post-photo { border-radius: 7px; }
  .post-left { left: 48px; top: 519px; width: 148px; height: 97px;
    background: linear-gradient(180deg, #b9b3a8 0%, #8f8a80 60%, #6e6a64 100%); }
  .post-featured { left: 209px; top: 516px; width: 275px; height: 184px;
    background: linear-gradient(180deg, #d5d8da 0%, #c6c9cb 45%, #9ea1a2 75%, #7d7f80 100%); }
  .post-right { left: 500px; top: 603px; width: 145px; height: 97px;
    background: radial-gradient(ellipse at 50% 55%, #3a3b3d 0%, var(--photo-night) 75%); }
  .dot { width: 11px; height: 11px; border-radius: 50%; border: 1px solid rgba(255,255,255,.9); background: rgba(255,255,255,.35); }
  .pill { height: 20px; border-radius: 10px; font-size: 6.5px; display: flex; align-items: center; justify-content: center; }
  .pill-solid { background: var(--white); color: var(--muted); }
  .pill-ghost { border: 1px solid rgba(255,255,255,.8); color: var(--white); }
  .featured-tab { left: 349px; top: 631px; width: 135px; height: 69px; background: var(--white); border-radius: 12px 0 8px 0; padding: 10px 0 0 12px; }
  .featured-tab .kicker { font-size: 14.5px; font-weight: 400; color: var(--muted); }
  .featured-tab .label { font-size: 24px; font-weight: 800; font-style: italic; color: var(--teal); line-height: 1.1; }
  .post-meta { font-size: 8px; color: var(--muted); }
  .post-title { font-size: 13px; font-weight: 700; line-height: 15.5px; color: var(--ink); width: 150px; }
</style>
</head>
<body>
  <main class="page">
    <header>
      <div class="abs brand">SPOKEWISE</div>
      <nav class="nav abs">
        <a href="#" style="left:251px">Discover</a>
        <a href="#" style="left:301px">Staff Picks</a>
        <a href="#" style="left:361px">Trending</a>
        <a href="#" style="left:416px">Videos</a>
      </nav>
      <a class="abs subscribe">Subscribe</a>
    </header>

    <section class="hero">
      <h1 class="abs hero-title">Innovative Cycling Products</h1>
      <p class="abs hero-text">Lorem ipsum dolor sit amet consectetur. Aliquet libero id sodales sit. Et et tempus et neque quam pulvinar vulputate quis. Leo lectus sapien ut netus urna luctus habitasse. Vitae tortor sapien arcu ultrices lectus amet amet.</p>
      <div class="abs photo photo-handlebar" role="img" aria-label="Close-up photo of road bike drop handlebars"></div>
      <div class="abs photo trending-card" role="img" aria-label="Photo of a bicycle on a wet coastal road with its reflection"></div>
      <h2 class="abs trending-title">Trending Now</h2>
      <a class="abs trending-link">View All</a>
    </section>

    <section class="posts">
      <h2 class="abs section-title">All Posts...</h2>

      <div class="abs post-photo post-left" role="img" aria-label="Photo of a bike leaning on a graffiti wall"></div>
      <span class="abs dot" style="left:176px;top:526px"></span>
      <p class="abs post-meta" style="left:48px;top:637px">, Blog Posts</p>
      <h3 class="abs post-title" style="left:48px;top:651px">Lorem ipsum dolor sitametconsectetur. Aliquet libero id</h3>

      <div class="abs post-photo post-featured" role="img" aria-label="Photo of two road cyclists riding by the sea"></div>
      <span class="abs dot" style="left:466px;top:596px"></span>
      <span class="abs dot" style="left:466px;top:610px"></span>
      <span class="abs pill pill-solid" style="left:217px;top:671px;width:69px">Dec 27, 2024</span>
      <span class="abs pill pill-ghost" style="left:290px;top:671px;width:52px">Dec 27, 2024</span>
      <div class="abs featured-tab">
        <p class="kicker">Blog Posts</p>
        <p class="label">Featured</p>
      </div>

      <p class="abs post-meta" style="left:501px;top:519px">, Blog Posts</p>
      <h3 class="abs post-title" style="left:501px;top:533px">Lorem ipsum dolor sitametconsectetur. Aliquet libero id</h3>
      <div class="abs post-photo post-right" role="img" aria-label="Photo of a dark mountain bike on a black background"></div>
      <span class="abs dot" style="left:626px;top:611px"></span>
    </section>
  </main>
</body>
</html>
```